Business Card Design

My company is a Consulting & Training company (Halvorn Consulting and Training, LLC) specializing in Firearms Training, State of Florida Concealed Weapons Permit Course, and Tactical Equipment Consulting.

Industry/Entity Type

Business

Contact Information for Business Card

Tobin Halvorn
P.O. Box 412763
Aventura, FL 33197
(786)555-0148

```html
<!DOCTYPE html>
<html lang="en">
<head>
<meta charset="utf-8">
<title>Halvorn Consulting and Training – Business Card</title>
<link rel="stylesheet" href="https://fonts.googleapis.com/css2?family=Orbitron:wght@500;700;800&display=swap">
<style>
  :root {
    --page: #ffffff;
    --camo-dark: #1e1e1f;
    --camo-mid: #3a3a3c;
    --camo-light: #55555a;
    --brand-red: #e0242b;
    --text-light: #f2f2f2;
  }
  * { box-sizing: border-box; margin: 0; padding: 0; }
  html, body {
    width: 1004px; height: 1200px; overflow: hidden;
    background: var(--page);
  }
  body { position: relative; font-family: "Orbitron", sans-serif; }

  .card {
    position: absolute; left: 17px; width: 972px; height: 569px;
    overflow: hidden;
    box-shadow: 0 1px 3px rgba(0,0,0,0.35);
  }
  .card--front { top: 18px; }
  .card--back { top: 610px; }

  .card__texture {
    position: absolute; inset: 0;
    background:
      radial-gradient(ellipse at 30% 35%, var(--camo-light) 0%, transparent 45%),
      radial-gradient(ellipse at 75% 70%, var(--camo-mid) 0%, transparent 50%),
      linear-gradient(160deg, var(--camo-mid) 0%, var(--camo-dark) 60%, #151516 100%);
  }

  .brand-mark {
    position: absolute; left: 0; right: 0;
    display: flex; justify-content: center; align-items: center; gap: 16px;
    color: var(--brand-red); font-weight: 800; letter-spacing: 2px;
  }
  .brand-mark__square { background: var(--brand-red); display: block; }

  .card--front .brand-mark { top: 120px; font-size: 58px; }
  .card--front .brand-mark__square { width: 44px; height: 44px; }

  .holder-name {
    position: absolute; top: 288px; left: 0; right: 0; text-align: center;
    color: var(--text-light); font-size: 54px; font-weight: 700; letter-spacing: 6px;
    text-transform: uppercase;
  }
  .holder-title {
    position: absolute; top: 352px; left: 0; right: 0; text-align: center;
    color: var(--brand-red); font-size: 22px; font-weight: 700; letter-spacing: 3px;
    text-transform: uppercase;
  }

  .contact {
    position: absolute; font-size: 24px; font-weight: 700; letter-spacing: 2px;
    color: var(--text-light); text-transform: uppercase; line-height: 31px;
  }
  .contact em { font-style: normal; color: var(--brand-red); }
  .contact--address { left: 55px; top: 430px; }
  .contact--phone { right: 52px; top: 492px; }

  .card--back .brand-mark { top: 120px; }
  .card--back .brand-mark__square { width: 190px; height: 190px; }
  .company {
    position: absolute; left: 0; right: 0; top: 350px; text-align: center;
    color: var(--brand-red); font-weight: 800; text-transform: uppercase;
  }
  .company__name { display: block; font-size: 60px; letter-spacing: 5px; line-height: 72px; }
  .company__tag { display: block; font-size: 25px; letter-spacing: 2px; line-height: 32px; }
  .company__form { display: block; font-size: 18px; letter-spacing: 2px; line-height: 24px; }
</style>
</head>
<body>

<section class="card card--front">
  <div class="card__texture" role="img" aria-label="Grey digital camouflage fabric background"></div>
  <div class="brand-mark">
    <span class="brand-mark__square"></span>
    <span class="brand-mark__name">HALVORN</span>
  </div>
  <h1 class="holder-name">Tobin Halvorn</h1>
  <p class="holder-title">Owner/Operator</p>
  <address class="contact contact--address">
    P.O. Box <em>412763</em><br>
    Aventura, FL<br>
    <em>33197</em>
  </address>
  <p class="contact contact--phone"><em>(786)</em>555-<em>0148</em></p>
</section>

<section class="card card--back">
  <div class="card__texture" role="img" aria-label="Grey digital camouflage fabric background"></div>
  <div class="brand-mark">
    <span class="brand-mark__square"></span>
  </div>
  <p class="company">
    <span class="company__name">Halvorn</span>
    <span class="company__tag">Consulting and Training</span>
    <span class="company__form">LLC</span>
  </p>
</section>

</body>
</html>
```